Tidewell Vitality Autumn Kickoff Quest advertisement design

We need an advertisement for a health, fitness and wellbeing company promoting a new service. The Autumn Kickoff Quest is a 10 week challenge where people choose from 2 program streams - either 1. Fat Loss or 2. Build Lean Muscle. Access to 40 group functional fitness sessions a week, access to exclusive discounts from Brisk Pantry Co. (BPC), discounts on personal training, a targeted gym program, full gym access for the duration of the Challenge and access to Exercise Physiologists and a Sports Dietitian. This is an Tidewell Vitality service co-branded with Brisk Pantry Co.. The final design should be in line with the style guide, be motivating and communicate a point of difference in the fitness industry.

Target Market(s)

men and women ages 30-50yrs, interested in improving their health and lifestyle

Industry/Entity Type

Fitness

Font styles to use
Other font styles liked:
• see style guide

Colors
000000
5c5c5c
9d9d9d
33b8a4
00a990

Requirements
Must have
• professional and exclusive look and feel, motivating tone
Nice to have
• clean design, not too overcrowding, use key pieces of information only and try to stay within the style guide for colour scheme (what is indicated below is the closest pick to our style guide but colour codes are within)
Should not have
• My project should not have any images that cheapen the challenge to look more like a general gym or body sculpting boot camp

```html
<!DOCTYPE html>
<html lang="en">
<head>
<meta charset="utf-8">
<title>Tidewell Vitality – Autumn Kickoff Quest</title>
<link rel="stylesheet" href="https://fonts.googleapis.com/css2?family=Josefin+Sans:wght@300;400;600;700&display=swap">
<style>
  :root {
    --black: #000000;
    --ink: #111111;
    --grey: #5c5c5c;
    --light-grey: #9d9d9d;
    --teal: #33b8a4;
    --teal-deep: #00a990;
    --white: #ffffff;
  }
  * { margin: 0; padding: 0; box-sizing: border-box; }
  html, body { width: 849px; height: 1200px; overflow: hidden; background: var(--black); }
  body { font-family: "Josefin Sans", "Century Gothic", sans-serif; }

  .poster { position: relative; width: 849px; height: 1200px; background: var(--black); overflow: hidden; }

  .dotted-rule { position: absolute; left: 40px; right: 40px; border-top: 4px dotted var(--white); }
  .rule-top { top: 96px; }
  .rule-title { top: 280px; }
  .rule-band { top: 826px; }
  .rule-foot { top: 1058px; }

  .duration-tag {
    position: absolute; left: 14px; top: 12px; width: 210px; height: 58px;
    background: var(--teal); color: var(--white); transform: rotate(-4deg);
    font-size: 36px; font-weight: 400; letter-spacing: 2px;
    display: flex; align-items: center; justify-content: center; padding-top: 6px;
  }

  .title { position: absolute; left: 0; right: 0; top: 104px; text-align: center; }
  .title-kicker { color: var(--white); font-size: 46px; font-weight: 300; letter-spacing: 3px; }
  .title-main { color: var(--teal); font-size: 104px; font-weight: 400; letter-spacing: 10px; line-height: 1; margin-top: 8px; }

  .benefits { position: absolute; left: 0; right: 0; top: 302px; height: 420px; background: var(--white); }
  .divider { position: absolute; background: var(--teal); }
  .divider-left-v { left: 330px; top: 62px; width: 3px; height: 300px; }
  .divider-right-v { left: 530px; top: 62px; width: 3px; height: 300px; }
  .divider-left-h { left: 50px; top: 200px; width: 280px; height: 3px; }
  .divider-right-h { left: 533px; top: 200px; width: 270px; height: 3px; }

  .benefit { position: absolute; text-align: center; line-height: 1; }
  .ink { color: var(--ink); }
  .teal { color: var(--teal); }
  .soft { color: var(--grey); }

  .gym-access { left: 50px; width: 280px; top: 42px; }
  .gym-access .big { font-size: 58px; font-weight: 300; }
  .gym-access .small { font-size: 26px; font-weight: 600; letter-spacing: 2px; margin-top: 4px; }

  .partner-offer { left: 50px; width: 280px; top: 222px; }
  .partner-offer .lead { font-size: 32px; font-weight: 300; }
  .partner-offer .sub { font-size: 24px; margin-top: 8px; }
  .partner-offer .name-big { font-size: 84px; font-weight: 400; margin-top: 4px; }
  .partner-offer .name-full { font-size: 18px; margin-top: 2px; }

  .group-sessions { left: 333px; width: 197px; top: 62px; }
  .group-sessions .count { font-size: 96px; font-weight: 400; }
  .group-sessions .per { font-size: 28px; color: var(--teal); vertical-align: top; position: relative; top: 14px; }
  .group-sessions .label { font-size: 44px; font-weight: 600; margin-top: 16px; line-height: 1.1; }
  .group-sessions .unit { font-size: 38px; font-weight: 300; margin-top: 6px; }

  .gym-program { left: 533px; width: 270px; top: 48px; }
  .gym-program .lead { font-size: 32px; font-weight: 300; }
  .gym-program .big { font-size: 72px; font-weight: 400; margin-top: 6px; }
  .gym-program .sub { font-size: 32px; font-weight: 300; margin-top: 4px; }

  .expert-access { left: 533px; width: 270px; top: 232px; }
  .expert-access .big { font-size: 56px; font-weight: 400; }
  .expert-access .sub { font-size: 22px; font-weight: 400; margin-top: 10px; line-height: 1.25; }

  .streams-band {
    position: absolute; left: 14px; right: 14px; top: 744px; height: 58px;
    background: var(--teal); color: var(--white);
    display: flex; align-items: center; justify-content: center; padding-top: 5px;
    font-size: 36px; font-weight: 600; letter-spacing: 3px;
  }
  .streams-band .or { font-weight: 300; font-size: 30px; margin: 0 14px; letter-spacing: 1px; }

  .brand { position: absolute; left: 0; right: 0; top: 872px; text-align: center; }
  .brand-name { color: var(--teal); font-size: 86px; font-weight: 400; letter-spacing: 6px; line-height: 1; }
  .brand-tagline { color: var(--teal); font-size: 30px; font-weight: 400; letter-spacing: 4px; margin-top: 38px; word-spacing: 30px; }
</style>
</head>
<body>
<main class="poster">
  <div class="duration-tag">10-WEEK</div>
  <div class="dotted-rule rule-top"></div>

  <header class="title">
    <div class="title-kicker">AUTUMN KICKOFF</div>
    <div class="title-main">QUEST</div>
  </header>
  <div class="dotted-rule rule-title"></div>

  <section class="benefits">
    <div class="divider divider-left-v"></div>
    <div class="divider divider-right-v"></div>
    <div class="divider divider-left-h"></div>
    <div class="divider divider-right-h"></div>

    <div class="benefit gym-access">
      <div class="big ink">FULL</div>
      <div class="big ink">GYM</div>
      <div class="small teal">ACCESS</div>
    </div>

    <div class="benefit partner-offer">
      <div class="lead ink">EXCLUSIVE</div>
      <div class="sub teal">Discounts from</div>
      <div class="name-big teal">BPC</div>
      <div class="name-full soft">Brisk Pantry Co.</div>
    </div>

    <div class="benefit group-sessions">
      <div class="count ink">40<span class="per">/wk</span></div>
      <div class="label teal">GROUP<br>FITNESS</div>
      <div class="unit ink">Sessions</div>
    </div>

    <div class="benefit gym-program">
      <div class="lead ink">TARGETED</div>
      <div class="big teal">GYM</div>
      <div class="sub ink">Program</div>
    </div>

    <div class="benefit expert-access">
      <div class="big teal">ACCESS</div>
      <div class="sub ink">Exercise Physiologist<br>&amp; Sports Dietician</div>
    </div>
  </section>

  <div class="streams-band">FAT LOSS<span class="or">or</span>BUILD LEAN MUSCLE</div>
  <div class="dotted-rule rule-band"></div>

  <footer class="brand">
    <div class="brand-name">TIDEWELL VITALITY</div>
    <div class="brand-tagline">HEALTH WELLBEING FITNESS</div>
  </footer>
  <div class="dotted-rule rule-foot"></div>
</main>
</body>
</html>
```